Harlowe Wine Label - Design a front and smaller back label for an exclusive red wine

Harlowe Wines produces a very high quality, high priced wine from an old and prestigous vineyard in one of Australia's oldest, but smallest wine growing regions. The grapevines are old (like old men with gnarled arms and trunks) and they produce fewer grapes than younger vines but the grape quality (and thus wine quality) is magnificent and highly sought after as it produces wine of exceptional quality.
The vineyard was purchased by the Harlowe family in February 2010 from a multinational wine company who made wonderful, trophy winning wines for 10 years before the vineyard went into a decline.
The challenge is to produce 2 labels - a simple main front label that focuses on the Harlowe brand and a smaller, information rich, back label that relates the history of the vineyard.
The labels should have a white or charcoal grey background and impart tradition, quality, exclusivity and a little self indulgence which is why we want the family crest incorporated - the choice of font will help.
It might also impart a sense of fun so that it appeals to the 25-35 year old age bracket.
The label should be kept clean and simple not loud and busy. Preferred colours are black, grey and white. Red is fine if used sparingly

Here are the details:_

Front Label (115 long x 65-90mm wide)

Harlowe
Lanternfield Reserve
2011
Mudgee
Wine of Australia 750ml

Back Label (dimensions to suit text and front label design; font size small; text in black so that it is readable in less than optimal light (eg candlelight at a restaurant table).

Harlowe
Lanternfield Reserve 2011

This is the first release of The Lanternfield’s Reserve – just 100 dozen bottles were made. The wine was made from Shiraz and 10% Cabernet Sauvignon grapes sourced from an iconic Mudgee vineyard that was established 1966 by Peter Kell. In 1994, the vineyard known as ”Silverbrook”, became the source of a decade of formidable, trophy winning wines under Ashgrove’s and later Penwick’s ownership. The 20ha vineyard was purchased by Morag & Helen Harlowe in 2010. The Silverbrook name was retained by Penwicks; no wine has been released under this label since the 2006 vintage.

The shaky old Shiraz vines are slowly being restored to full health using careful cane pruning techniques that stimulates fresh, new tissue growth, more even bunch sizes and better grape quality and consistency. The Shiraz grapes used in this wine were hand-picked from two rows of the first crop from the 46 year old, cane pruned vines. The 2011 Reserve is the first step to re-establish the traditions of a famous vineyard and one of Australia’s most sought after export wines.

“Deep and intense purple hues with aromas of ripe blackberry fruits, spice and eucalypt with rich chocolate complemented by subtle oak overtones. A rich and full bodied wine exhibiting a soft yet generous palate with plum, forest fruits and mint chocolate notes. A fine grained tannin structure displaying integrated oak characters adds to the complexity of the wine. This wine was aged for 18 months in a blend of new French oak hogsheads and one year old American hogsheads, crafting a blend with great structure and length of flavour which will develop into a Mudgee classic” – Owen Pratley, Winemaker

13.5% Alc/Vol.
Contains approx 8.0 std drinks
Preservative (220) added

Harlowe Wines
Tallowby Rd, Mudgee 2850
www.harlowewines-example.com.au

Reason: My apologies to the designers who have kindly submitted some wonderful designs. I am trying to achieve a conscentious between shareholders. This is difficult as they are in different parts of the world and I have learned through this experience that opinions on wine labels are quite diverse!!! The feedback I have received so far indicates the following (1) A light or white background is preferred (2) The crest should not be a dominant part of the label (3) The label needs to be clean, fresh and uncomplicated (4) If red is used it should be in minor detail only (5) "Harlowe" should be distinctive. The font is difficult for us! (6) We are considering "The Lanternfield" RESERVE instead of "Lanternfield" RESERVE (7) The text on the back label is too long; I will edit and re-upload Many thanks for your help and patience Kind regards Morag

Good Morning All,
I have edited the back label text to reduce the size of the label. A Word file with the changes has just been uploaded.
Cheers
Morag

Dear Designers,
Thank you all so very much for the wonderful selection of designs you have submitted my family have all been overwhelmed by the quality and skill level exhibited and we all appreciate you your efforts
Kindest regards
Morag

Target Market(s)

25-35 year old men and women of Australia, China, US & UK

Industry/Entity Type

Restaurant

Requirements
Must have
• Crest
Should not have
• Animals on the label

```html
<!DOCTYPE html>
<html lang="en">
<head>
<meta charset="utf-8">
<title>Harlowe Lanternfield Reserve – Front and Back Labels</title>
<link rel="stylesheet" href="https://fonts.googleapis.com/css2?family=Oswald:wght@300;400&family=Roboto+Condensed:wght@400;700&display=swap">
<style>
  :root {
    --red: #e8202a;
    --ink: #1a1a1a;
    --paper: #ffffff;
    --crest: #c9c9c9;
    --emblem: #7a1418;
    --bg: #ffffff;
  }
  * { margin: 0; padding: 0; box-sizing: border-box; }
  html, body { width: 1200px; height: 900px; overflow: hidden; background: var(--bg); }
  .canvas { position: relative; width: 1200px; height: 900px; }

  /* Front label */
  .front-label {
    position: absolute; left: 70px; top: 262px; width: 278px; height: 490px;
    background: var(--paper); box-shadow: 0 1px 3px rgba(0,0,0,.18); overflow: hidden;
  }
  .front-label .red-field { position: absolute; left: 0; top: 0; width: 100%; height: 195px; background: var(--red); }
  .front-label .teeth { position: absolute; left: 0; top: 195px; width: 100%; height: 12px; }
  .front-label .frame { position: absolute; inset: 12px; border: 1px solid var(--ink); }
  .emblem {
    position: absolute; left: 194px; top: 30px; width: 64px; height: 64px;
    border-radius: 50%; background: var(--emblem); border: 2px solid var(--ink);
  }
  .front-label .vintage {
    position: absolute; left: 30px; top: 166px;
    font: 400 30px/1 "Oswald", sans-serif; color: var(--ink); letter-spacing: 1px;
  }
  .front-label .wine-name {
    position: absolute; left: 30px; top: 230px; width: 220px;
    font: 300 31px/36px "Oswald", sans-serif; color: var(--ink);
    letter-spacing: 1.5px; text-transform: uppercase; white-space: nowrap;
  }
  .front-label .region {
    position: absolute; left: 30px; top: 366px;
    font: 700 14px/19px "Roboto Condensed", sans-serif; color: var(--ink);
  }
  .front-label .volume {
    position: absolute; left: 30px; top: 418px;
    font: 700 14px/1 "Roboto Condensed", sans-serif; color: var(--ink);
  }
  .crest {
    position: absolute; left: 176px; top: 330px; width: 80px; height: 124px;
    background: linear-gradient(180deg, #e4e4e4, var(--crest));
    border-radius: 4px 4px 40px 40px;
  }

  /* Back label */
  .back-label {
    position: absolute; left: 381px; top: 262px; width: 276px; height: 490px;
    background: var(--red); box-shadow: 0 1px 3px rgba(0,0,0,.18); overflow: hidden;
  }
  .back-label .frame { position: absolute; inset: 8px; border: 1px solid var(--paper); }
  .back-label .brand-small {
    position: absolute; left: 0; top: 19px; width: 100%; text-align: center;
    font: 400 11px/1 "Oswald", sans-serif; color: var(--paper); letter-spacing: 3px;
  }
  .back-label .brand-small::before, .back-label .brand-small::after {
    content: ""; display: inline-block; width: 70px; height: 1px; background: var(--paper);
    vertical-align: middle; margin: 0 8px;
  }
  .back-label .wine-name {
    position: absolute; left: 0; top: 30px; width: 100%; text-align: center;
    font: 400 18px/1 "Oswald", sans-serif; color: var(--paper); letter-spacing: 2.2px;
    text-transform: uppercase;
  }
  .back-label .vintage {
    position: absolute; left: 20px; right: 20px; top: 51px; text-align: center;
    font: 400 10px/1 "Oswald", sans-serif; color: var(--paper); letter-spacing: 2px;
    border-top: 1px solid var(--paper); padding-top: 1px;
  }
  .story-panel { position: absolute; left: 0; top: 62px; width: 100%; height: 320px; background: var(--paper); }
  .story-panel .teeth { position: absolute; left: 0; width: 100%; height: 10px; }
  .story-panel .teeth.top { top: 0; }
  .story-panel .teeth.bottom { bottom: 0; }
  .story {
    position: absolute; left: 12px; right: 12px; top: 15px; bottom: 13px;
    column-count: 2; column-gap: 10px; column-fill: auto;
    font: 400 8.1px/9.6px "Roboto Condensed", sans-serif; color: var(--ink);
    text-align: justify; hyphens: auto; overflow: hidden;
  }
  .story p { margin-bottom: 8px; }
  .back-label .legal {
    position: absolute; left: 0; top: 392px; width: 100%; text-align: center;
    font: 400 10.5px/12px "Roboto Condensed", sans-serif; color: var(--paper);
  }
  .key {
    position: absolute; top: 424px; width: 56px; height: 14px;
    background: rgba(255,255,255,.55); border-radius: 7px;
  }
  .key.left { left: 18px; }
  .key.right { right: 18px; }
  .back-label .producer {
    position: absolute; left: 0; top: 420px; width: 100%; text-align: center;
    font: 400 17px/1 "Oswald", sans-serif; color: var(--paper); letter-spacing: 2px;
    text-transform: uppercase;
  }
  .back-label .address {
    position: absolute; left: 0; top: 449px; width: 100%; text-align: center;
    font: 400 10px/1 "Roboto Condensed", sans-serif; color: var(--paper);
  }
  .back-label .web {
    position: absolute; left: 0; top: 463px; width: 100%; text-align: center;
    font: 700 8.5px/1 "Roboto Condensed", sans-serif; color: var(--paper); letter-spacing: .8px;
  }
</style>
</head>
<body>
<main class="canvas">

  <section class="front-label" aria-label="Front label">
    <div class="red-field"></div>
    <svg class="teeth" viewBox="0 0 278 12" preserveAspectRatio="none" aria-hidden="true">
      <defs>
        <pattern id="front-teeth" width="13.9" height="12" patternUnits="userSpaceOnUse">
          <path d="M0 0H13.9L6.95 12Z" fill="#e8202a"/>
        </pattern>
      </defs>
      <rect width="278" height="12" fill="url(#front-teeth)"/>
    </svg>
    <div class="frame"></div>
    <div class="emblem" role="img" aria-label="Round emblem with crossed keys"></div>
    <div class="vintage">2011</div>
    <h1 class="wine-name">Harlowe<br>Lanternfield<br>Reserve</h1>
    <p class="region">Mudgee<br>Wine of Australia</p>
    <p class="volume">750ml</p>
    <div class="crest" role="img" aria-label="Family crest drawing"></div>
  </section>

  <section class="back-label" aria-label="Back label">
    <div class="frame"></div>
    <div class="brand-small">HARLOWE</div>
    <h2 class="wine-name">Lanternfield Reserve</h2>
    <div class="vintage">2011</div>

    <div class="story-panel">
      <svg class="teeth top" viewBox="0 0 276 10" preserveAspectRatio="none" aria-hidden="true">
        <defs>
          <pattern id="teeth-down" width="13.8" height="10" patternUnits="userSpaceOnUse">
            <path d="M0 0H13.8L6.9 10Z" fill="#e8202a"/>
          </pattern>
          <pattern id="teeth-up" width="13.8" height="10" patternUnits="userSpaceOnUse">
            <path d="M0 10H13.8L6.9 0Z" fill="#e8202a"/>
          </pattern>
        </defs>
        <rect width="276" height="10" fill="url(#teeth-down)"/>
      </svg>
      <div class="story">
        <p>This is the first release of the Lanternfield Reserve – just 100 dozen bottles were made. The wine was made from Shiraz and 10% Cabernet Sauvignon grapes sourced from an iconic Mudgee vineyard that was established 1966 by Peter Kell. In 1994, the vineyard known as “Silverbrook”, became the source of a decade of formidable, trophy winning wines under Ashgrove’s and later Penwick’s ownership. The 20ha vineyard was purchased by Morag &amp; Helen Harlowe in 2010. The Silverbrook name was retained by Penwicks; no wine has been released under this label since the 2006 vintage.</p>
        <p>The shaky old Shiraz vines are slowly being restored to full health using careful cane pruning techniques that stimulates fresh, new tissue growth, more even bunch sizes and better grape quality and consistency. The Shiraz grapes used in this wine were hand-picked from two rows of the first crop from the 46 year old, cane pruned vines. The 2011 Reserve is the first step to re-establish the traditions of a famous vineyard and one of Australia’s most sought after export wines.</p>
        <p>“Deep and intense purple hues with aromas of ripe blackberry fruits, spice and eucalypt with rich chocolate complemented by subtle oak overtones. A rich and full bodied wine exhibiting a soft yet generous palate with plum, forest fruits and mint chocolate notes. A fine grained tannin structure displaying integrated oak characters adds to the complexity of the wine. This wine was aged for 18 months in a blend of new French oak hogsheads and one year old American hogsheads, crafting a blend with great structure and length of flavour which will develop into a Mudgee classic” – Owen Pratley, Winemaker</p>
      </div>
      <svg class="teeth bottom" viewBox="0 0 276 10" preserveAspectRatio="none" aria-hidden="true">
        <rect width="276" height="10" fill="url(#teeth-up)"/>
      </svg>
    </div>

    <p class="legal">13.5% Alc/Vol. Contains approx 8.0 std drinks<br>Preservative (220) added</p>
    <div class="key left" role="img" aria-label="Ornamental key"></div>
    <div class="key right" role="img" aria-label="Ornamental key"></div>
    <p class="producer">Harlowe</p>
    <p class="address">Harlowe Wines Tallowby Rd, Mudgee 2850</p>
    <p class="web">www.harlowewines-example.com.au</p>
  </section>

</main>
</body>
</html>
```